We need visit card and a letter paper for our website. thx

We have a beauty clinic in Switzerland.
https://wolkenbachtal.ch
We need a visit card.

Requirements
Must have
• see colors on website

```html
<!DOCTYPE html>
<html lang="en">
<head>
<meta charset="utf-8">
<title>Wolkenbachtal Letterhead</title>
<link rel="stylesheet" href="https://fonts.googleapis.com/css2?family=Poppins:wght@300;400;600&family=Arimo:wght@400&display=swap">
<style>
  :root {
    --backdrop: #e4e4e4;
    --paper: #ffffff;
    --ink: #1f1f1f;
    --ink-soft: #3d3d3d;
    --body-ink: #3a3a3a;
    --greeting-ink: #4a4a4a;
    --signature-tone: #d9d9d9;
  }
  * { margin: 0; padding: 0; box-sizing: border-box; }
  html, body {
    width: 1098px; height: 1200px; overflow: hidden;
    background: var(--backdrop);
  }
  .letter {
    position: absolute; left: 121px; top: 0;
    width: 856px; height: 1200px;
    background: var(--paper);
    font-family: "Arimo", Arial, sans-serif;
    color: var(--body-ink);
  }
  .brand {
    position: absolute; left: 87px; top: 82px;
    font-family: "Poppins", sans-serif;
    font-weight: 300; font-size: 24px; letter-spacing: 0.2px;
    color: var(--ink);
  }
  .contact {
    position: absolute; right: 72px; top: 64px;
    font-family: "Poppins", sans-serif;
    text-align: right;
    color: var(--ink-soft);
  }
  .contact-group { margin-bottom: 22px; }
  .contact-group.tight { margin-bottom: 20px; }
  .contact-line {
    display: flex; justify-content: flex-end; align-items: center;
    font-size: 13px; font-weight: 300; line-height: 16px;
  }
  .contact-line.name {
    font-size: 14.5px; font-weight: 600; color: var(--ink); line-height: 19px;
  }
  .icon {
    width: 12px; height: 12px; margin-left: 9px; flex: none;
    fill: var(--ink);
  }
  .icon-spacer { width: 12px; margin-left: 9px; flex: none; }
  .greeting {
    position: absolute; left: 64px; top: 310px;
    font-size: 20px; color: var(--greeting-ink);
  }
  .body-copy {
    position: absolute; left: 64px; top: 361px; width: 727px;
    font-size: 12.2px; line-height: 18.3px; text-align: justify;
    hyphens: auto;
  }
  .body-copy p { margin-bottom: 18.3px; }
  .closing {
    position: absolute; left: 64px; top: 763px;
    font-size: 12.2px;
  }
  .signature {
    position: absolute; left: 50px; top: 794px;
    width: 166px; height: 66px;
    background: linear-gradient(90deg, var(--paper), var(--signature-tone) 50%, var(--paper));
    opacity: 0.6;
  }
</style>
</head>
<body>
<main class="letter">
  <div class="brand">Wolkenbachtal</div>

  <address class="contact">
    <div class="contact-group tight">
      <div class="contact-line name">Dr. Lena Arbogast
        <svg class="icon" viewBox="0 0 12 12"><circle cx="6" cy="3.3" r="2.8"/><path d="M0.8 12c0-3.6 2.3-5.4 5.2-5.4s5.2 1.8 5.2 5.4z"/></svg>
      </div>
      <div class="contact-line">Plastische Chirurgie<span class="icon-spacer"></span></div>
    </div>
    <div class="contact-group">
      <div class="contact-line name">Dr. Moser Tobias, DESA
        <svg class="icon" viewBox="0 0 12 12"><circle cx="6" cy="3.3" r="2.8"/><path d="M0.8 12c0-3.6 2.3-5.4 5.2-5.4s5.2 1.8 5.2 5.4z"/></svg>
      </div>
      <div class="contact-line">FA für Anästhesist<span class="icon-spacer"></span></div>
    </div>
    <div class="contact-group">
      <div class="contact-line">Lindenweg 12
        <svg class="icon" viewBox="0 0 12 12"><path d="M6 0a4.3 4.3 0 0 0-4.3 4.3C1.7 7.5 6 12 6 12s4.3-4.5 4.3-7.7A4.3 4.3 0 0 0 6 0zm0 6.1a1.8 1.8 0 1 1 0-3.6 1.8 1.8 0 0 1 0 3.6z"/></svg>
      </div>
      <div class="contact-line">7499 Ardezberg<span class="icon-spacer"></span></div>
      <div class="contact-line">Schweiz<span class="icon-spacer"></span></div>
    </div>
    <div class="contact-group">
      <div class="contact-line">+41 (0) 800 24 60 60
        <svg class="icon" viewBox="0 0 12 12"><path d="M2.4 0.5l2 2.2-1.1 1.6c.7 1.7 2.1 3.1 3.8 3.8l1.6-1.1 2.2 2-1.2 2.3C5 10.9 1.1 7 .1 1.7z"/></svg>
      </div>
      <div class="contact-line">hallo@wolkenbachtal.ch
        <svg class="icon" viewBox="0 0 12 12"><path d="M0.5 2.2h11v1L6 6.6 0.5 3.2z"/><path d="M0.5 4.4L6 7.8l5.5-3.4v5.4h-11z"/></svg>
      </div>
      <div class="contact-line">wolkenbachtal.ch
        <svg class="icon" viewBox="0 0 12 12"><circle cx="6" cy="6" r="5.5"/><path d="M3 4.2c1 .2 1.6 1 1.4 2 1 .4 1 1.6.6 2.6M8 2.5c-.6.8-.4 1.8.6 2.1.9.3 1.2 1 1 1.9" stroke="#fff" stroke-width="1" fill="none"/></svg>
      </div>
    </div>
  </address>

  <h1 class="greeting" style="font-weight:400">Dear Mr. Keller,</h1>

  <section class="body-copy">
    <p>Lorem ipsum dolor sit amet, consectetur adipiscing elit. Donec orci purus, luctus vitae dignissim eu, iaculis sed purus. Vivamus faucibus, ipsum nec aliquet viverra, leo mauris condimentum ligula, sit amet sagittis enim ligula quis arcu. Nam egestas tortor id nisi porttitor mattis. In tortor ante, ultricies in suscipit a, tempus non massa. Vivamus et auctor mi. Fusce vel massa nulla. Phasellus nec eros mauris, et scelerisque orci.</p>
    <p>Donec malesuada orci vitae nulla accumsan porta a id massa. Quisque accumsan iaculis magna sit amet fringilla. Maecenas consequat, magna eget tincidunt semper, odio nibh rutrum mi, id feugiat ante nisi eu risus. Vestibulum nunc orci, rhoncus a placerat in, ultricies in mi. Cras mattis varius eros, vel fringilla nisi suscipit eget. Quisque scelerisque sagittis nulla at porttitor.</p>
    <p>Sed id augue vitae urna euismod commodo aliquet a quam. Pellentesque arcu velit, cursus et malesuada ut, consequat et diam. Nullam erat sem, rhoncus id ullamcorper vitae, rhoncus et arcu. In ultricies ultricies nulla, ut rutrum nisi iaculis at. Donec eu magna a metus ornare faucibus. Fusce aliquet faucibus ultricies. Morbi semper, est id tincidunt gravida, sem arcu adipiscing lacus, ac bibendum nulla leo eu purus. Quisque nec diam sed risus consectetur a ccumsan quis quis nibh. Vestibulum id purus lorem.</p>
    <p>It is a long established fact that a reader will be distracted by the readable content of a page when looking at its layout. The point of using Lorem Ipsum is that it has a more-or-less normal distribution of letters, as opposed to using 'Content here, content here', making it look like readable English. Many desktop publishing packages</p>
    <p>ada ut, consequat et diam. Nullam erat sem, rhoncus id ullamcorper vitae, rhoncus et arcu. In ultricies ultricies nulla, ut rutrum nisi iaculis at. Donec eu magna a metus ornare faucibus. Fusce aliquet faucibus ultricies. Morbi semper,</p>
  </section>

  <p class="closing">Sincerely,</p>
  <div class="signature" role="img" aria-label="Handwritten signature of Dr. Lena Arbogast"></div>
</main>
</body>
</html>
```